Need a design package for hair towels wrap

We need package design for hair towel wrap ( 3 pack) brand name is The Quorin. We are looking for simple, contemporary and unique design, color palette 2-3 colors. Paper Box size is 9*8*3 inches with PVC window.Actual picture of the product won't be on the package.Attached Brand Logo and description for the package. Barcode needed to be included on the design package.It will be provided later. Attached sample of the box from manufacturer, and instruction for towel wrap which idea I like, if you could make something similar to it, would be great.

Target Market(s)

Zelvora

Industry/Entity Type

Hair

Colors
848484
f5f5f5
faa54b
333333

Requirements
Must have
• Clean, contemporary design.

```html
<!DOCTYPE html>
<html lang="en">
<head>
<meta charset="utf-8">
<title>The Quorin – Microfiber Hair Towel Wrap Box Dieline</title>
<link rel="stylesheet" href="https://fonts.googleapis.com/css2?family=Roboto:wght@300;400;700&display=swap">
<style>
  :root {
    --stage: #464445;
    --sheet: #ffffff;
    --panel-grey: #a3a3a3;
    --window: #ececec;
    --ink: #848484;
    --ink-dark: #333333;
    --orange: #e9a23b;
    --white: #f5f5f5;
  }
  html, body { margin: 0; padding: 0; overflow: hidden; }
  body { width: 1200px; height: 900px; background: var(--stage); font-family: "Roboto", Arial, sans-serif; }
  .dieline { display: block; width: 1200px; height: 900px; }
  .sheet { fill: var(--sheet); }
  .panel-grey { fill: var(--panel-grey); }
  .window { fill: var(--window); }
  .flap { fill: url(#goldFlap); }
  .ornament-front { fill: url(#ornamentWhite); }
  .ornament-side { fill: url(#ornamentGrey); }
  .brand-mark { fill: var(--orange); }
  .brand-name { font-family: "Roboto", Arial, sans-serif; font-weight: 700; fill: var(--ink); letter-spacing: .5px; }
  .brand-name--white { fill: var(--white); }
  .tagline { font-weight: 400; font-size: 15px; fill: var(--ink-dark); }
  .product-title { font-weight: 400; font-size: 16px; fill: var(--ink); }
  .product-sub { font-weight: 400; font-size: 13px; fill: var(--orange); }
  .product-note { font-weight: 300; font-size: 8px; fill: var(--ink); }
  .benefit { font-weight: 400; font-size: 10.5px; fill: var(--white); }
  .size-pill { fill: var(--orange); }
  .size-text { font-weight: 400; font-size: 13px; fill: #ffffff; }
  .rule { stroke: var(--orange); stroke-width: 1.2; }
  .directions-title { font-weight: 300; font-size: 14px; fill: var(--orange); }
  .step-pill { fill: var(--orange); }
  .step-label { font-size: 6.5px; fill: #ffffff; font-weight: 700; }
  .step-text { font-weight: 300; font-size: 5px; fill: var(--ink-dark); }
  .step-art { fill: #f1f1f1; stroke: #d8d8d8; stroke-width: .6; }
  .cycle-arc { fill: none; stroke: var(--orange); stroke-width: 1.4; }
  .info-head { font-weight: 700; font-size: 7.5px; fill: #ffffff; }
  .info-text { font-weight: 400; font-size: 6.2px; fill: #ffffff; }
</style>
</head>
<body>
<svg class="dieline" viewBox="0 0 1200 900" xmlns="http://www.w3.org/2000/svg">
  <defs>
    <linearGradient id="goldFlap" x1="0" y1="0" x2="1" y2="1">
      <stop offset="0" stop-color="#c38f2c"/>
      <stop offset=".5" stop-color="#f6c96c"/>
      <stop offset="1" stop-color="#d9a040"/>
    </linearGradient>
    <linearGradient id="ornamentWhite" x1="0" y1="1" x2="1" y2="0">
      <stop offset="0" stop-color="#f3d49a" stop-opacity=".55"/>
      <stop offset=".6" stop-color="#f6dfb4" stop-opacity=".15"/>
      <stop offset="1" stop-color="#ffffff" stop-opacity="0"/>
    </linearGradient>
    <linearGradient id="ornamentGrey" x1="0" y1="1" x2="0" y2="0">
      <stop offset="0" stop-color="#e9c07a" stop-opacity=".45"/>
      <stop offset="1" stop-color="#a3a3a3" stop-opacity="0"/>
    </linearGradient>
  </defs>

  <rect class="sheet" x="123" y="96" width="954" height="708"/>

  <!-- Top flap with benefits (printed upside down) -->
  <polygon class="flap" points="192,100 468,100 490,143 170,143"/>
  <rect class="panel-grey" x="170" y="143" width="327" height="122"/>
  <g transform="rotate(180 333.5 204)">
    <text class="benefit" x="190" y="171">•&#160;&#160;Suitable for all hair types and lengths</text>
    <text class="benefit" x="190" y="188">•&#160;&#160;Holds extra-long hair</text>
    <text class="benefit" x="190" y="205">•&#160;&#160;Absorbs approximately 70% of water within 10 minutes</text>
    <text class="benefit" x="190" y="221">•&#160;&#160;Reduces risk of split ends, breakage, and frizz</text>
    <text class="benefit" x="190" y="237">•&#160;&#160;Lightweight, easy to pack and use at the gym or for travel</text>
    <text class="benefit" x="190" y="252">•&#160;&#160;Less blow-drying means healthier hair</text>
    <rect class="brand-mark" x="448" y="160" width="9" height="9"/>
    <text class="brand-name brand-name--white" x="420" y="187" font-size="10">THE QUORIN</text>
  </g>

  <!-- Glue tab -->
  <polygon class="flap" points="128,300 170,265 170,635 128,610"/>

  <!-- Front panel -->
  <g class="front-panel">
    <rect class="ornament-front" x="170" y="265" width="175" height="370" role="img" aria-label="Soft gold ribbon ornament sweeping across the front panel"/>
    <rect class="brand-mark" x="236" y="428" width="11" height="11"/>
    <text class="brand-name" font-size="17" text-anchor="middle" transform="translate(278 452) rotate(-90)">THE QUORIN</text>
    <text class="tagline" text-anchor="middle" transform="translate(301 450) rotate(-90)">Beautiful Hair Begins With The Right Towel</text>
    <rect class="window" x="311" y="318" width="107" height="265"/>
    <text class="product-title" text-anchor="middle" transform="translate(441 452) rotate(-90)">Microfiber Hair Towel Wrap</text>
    <text class="product-sub" text-anchor="middle" transform="translate(456 452) rotate(-90)">Set of 3 Hair Towels</text>
    <text class="product-note" text-anchor="middle" transform="translate(478 452) rotate(-90)">The softest, absorbent, lightest &amp; safest</text>
    <text class="product-note" text-anchor="middle" transform="translate(488 452) rotate(-90)">Towel for your hair.</text>
  </g>

  <!-- Left side panel -->
  <polygon class="flap" points="497,203 608,203 622,265 497,265"/>
  <rect class="panel-grey" x="497" y="265" width="125" height="370"/>
  <rect class="ornament-side" x="497" y="265" width="125" height="370" role="img" aria-label="Soft gold ribbon ornament on side panel"/>
  <rect class="brand-mark" x="542" y="455" width="11" height="11"/>
  <text class="brand-name brand-name--white" font-size="17" text-anchor="middle" transform="translate(604 470) rotate(-90)">THE QUORIN</text>
  <polygon class="flap" points="497,635 622,635 622,695 510,695"/>

  <!-- Back panel: directions -->
  <g class="back-panel">
    <text class="product-title" font-size="17" text-anchor="middle" transform="translate(922 450) rotate(90)">Microfiber Hair Towel Wrap</text>
    <text class="product-sub" font-size="14" text-anchor="middle" transform="translate(903 450) rotate(90)">Set of 3 Hair Towels</text>
    <line class="rule" x1="876" y1="285" x2="876" y2="618"/>
    <rect class="size-pill" x="865" y="350" width="23" height="222" rx="11.5"/>
    <text class="size-text" text-anchor="middle" transform="translate(872 461) rotate(90)">Hair Towel 26 x 10 inches</text>

    <path class="cycle-arc" d="M700,385 A90,88 0 0 1 700,558"/>
    <polygon class="brand-mark" points="696,381 706,383 700,391"/>
    <polygon class="brand-mark" points="696,562 706,560 700,552"/>
    <rect class="brand-mark" x="740" y="464" width="10" height="10"/>
    <text class="brand-name" font-size="9" text-anchor="middle" transform="translate(712 470) rotate(90)">THE QUORIN</text>
    <text class="directions-title" text-anchor="middle" transform="translate(692 470) rotate(90)">Directions</text>

    <rect class="step-art" x="722" y="338" width="46" height="48" role="img" aria-label="Line drawing: leaning forward with towel placed at nape"/>
    <rect class="step-pill" x="738" y="300" width="15" height="34" rx="7.5"/>
    <text class="step-label" text-anchor="middle" transform="translate(743 317) rotate(90)">step 1</text>
    <text class="step-text" transform="translate(718 300) rotate(90)">Lean your head forward and place</text>
    <text class="step-text" transform="translate(711 300) rotate(90)">the towel at the nape of your</text>
    <text class="step-text" transform="translate(704 300) rotate(90)">neck, hairline ends inside.</text>

    <rect class="step-art" x="795" y="462" width="52" height="66" role="img" aria-label="Line drawing: wrapping and twisting hair in towel"/>
    <rect class="step-pill" x="808" y="422" width="15" height="34" rx="7.5"/>
    <text class="step-label" text-anchor="middle" transform="translate(813 439) rotate(90)">step 2</text>
    <text class="step-text" transform="translate(789 408) rotate(90)">Wrap the towel around</text>
    <text class="step-text" transform="translate(782 408) rotate(90)">your hair and twist a</text>
    <text class="step-text" transform="translate(775 408) rotate(90)">few times.</text>

    <rect class="step-art" x="722" y="558" width="46" height="48" role="img" aria-label="Line drawing: towel secured on head with loop"/>
    <rect class="step-pill" x="738" y="522" width="15" height="34" rx="7.5"/>
    <text class="step-label" text-anchor="middle" transform="translate(743 539) rotate(90)">step 3</text>
    <text class="step-text" transform="translate(718 552) rotate(90)">Fold the twisted end up</text>
    <text class="step-text" transform="translate(711 552) rotate(90)">over your head and secure</text>
    <text class="step-text" transform="translate(704 552) rotate(90)">it with the loop.</text>
  </g>

  <!-- Right side panel -->
  <polygon class="flap" points="947,265 947,203 1058,203 1072,265"/>
  <rect class="panel-grey" x="947" y="265" width="125" height="370"/>
  <rect class="ornament-side" x="947" y="265" width="125" height="370" role="img" aria-label="Soft gold ribbon ornament on side panel"/>
  <rect class="brand-mark" x="989" y="455" width="11" height="11"/>
  <text class="brand-name brand-name--white" font-size="17" text-anchor="middle" transform="translate(965 460) rotate(90)">THE QUORIN</text>
  <polygon class="flap" points="947,635 1072,635 1058,695 947,695"/>

  <!-- Bottom panel: material & care -->
  <rect class="panel-grey" x="622" y="635" width="325" height="122"/>
  <text class="info-head" x="636" y="652">Material:</text>
  <text class="info-text" x="636" y="665">The <tspan font-weight="700">QUORIN</tspan> Hair Towel Wrap is made from innovative,</text>
  <text class="info-text" x="636" y="674">luxurious, light microfiber material for maximum absorption</text>
  <text class="info-text" x="636" y="683">and comfort. It will dry your hair up to 4 times faster than a</text>
  <text class="info-text" x="636" y="692">regular towel, and is soft, light, and gentle for both hair and</text>
  <text class="info-text" x="636" y="701">skin. The <tspan font-weight="700">QUORIN</tspan> will leave your hair healthy and silky.</text>
  <text class="info-text" x="828" y="658">80% polyester + 20% nylon</text>
  <text class="info-text" x="828" y="667">Machine wash, tumble dry low</text>
  <text class="info-text" x="828" y="676">temperature. No bleach. No softener.</text>
  <text class="info-text" x="828" y="685">Designed in USA</text>
  <rect x="878" y="680" width="12" height="7" fill="#d9d9d9"/>
  <rect x="878" y="680" width="5" height="4" fill="#3c4f8f"/>
  <text class="info-text" x="828" y="694">Made in China</text>
  <text class="info-head" x="636" y="722">Hair Care Tip:</text>
  <text class="info-text" x="636" y="734">Allow The <tspan font-weight="700">QUORIN</tspan> to absorb water from your hair naturally;</text>
  <text class="info-text" x="636" y="743">never rub your hair and scalp while using the towel.</text>
  <polygon class="flap" points="622,757 947,757 930,800 639,800"/>
</svg>
</body>
</html>
```